Refresh American History Book Cover

We would like a new book cover based on the attached old book cover. Please maintain a very strong resemblance to the cover, but we would be open to a bit of a freshening up of the design. We would like to use the same illustrations since they match the illustrations inside. Please fix the whale! It's head should not be cut off!

We are using this for Vextora Quillmark Self Printing in a 6" x 9" format.

```html
<!DOCTYPE html>
<html lang="en">
<head>
<meta charset="utf-8">
<title>Legends, Oysters, Lighthouses &amp; Tides — Book Cover</title>
<link rel="stylesheet" href="https://fonts.googleapis.com/css2?family=Montserrat:wght@600;700&family=EB+Garamond:wght@400&family=Cabin:ital,wght@1,400&display=swap">
<style>
  :root {
    --backdrop: #4d4d4d;
    --paper: #ffffff;
    --ink: #323232;
    --accent-blue: #3371e8;
    --subtitle-grey: #555555;
    --rule-grey: #cfcfcf;
    --illustration-paper: #f7ece6;
    --illustration-rust-soft: #d98f72;
  }
  html, body {
    margin: 0;
    padding: 0;
    width: 944px;
    height: 1200px;
    overflow: hidden;
    background: var(--backdrop);
  }
  .stage {
    display: block;
    width: 944px;
    height: 1200px;
  }
  .cover { fill: var(--paper); }
  .title-line {
    font-family: "Montserrat", "Helvetica Neue", Arial, sans-serif;
    font-weight: 700;
    font-size: 74px;
  }
  .title-line.dark { fill: var(--ink); }
  .title-line.blue { fill: var(--accent-blue); }
  .ampersand {
    font-family: "EB Garamond", Georgia, serif;
    font-size: 100px;
    fill: var(--ink);
  }
  .subtitle {
    font-family: "Cabin", "Gill Sans", sans-serif;
    font-style: italic;
    font-size: 20px;
    fill: var(--subtitle-grey);
  }
  .subtitle .initial { font-size: 26px; }
  .divider { stroke: var(--rule-grey); stroke-width: 1.5; }
  .author {
    font-family: "Montserrat", "Helvetica Neue", Arial, sans-serif;
    font-weight: 700;
    font-size: 23px;
    fill: var(--accent-blue);
  }
</style>
</head>
<body>
<svg class="stage" viewBox="0 0 944 1200" xmlns="http://www.w3.org/2000/svg">
  <defs>
    <linearGradient id="whale-tone" x1="0" y1="0" x2="0" y2="1">
      <stop offset="0" stop-color="var(--paper)"/>
      <stop offset="0.55" stop-color="var(--illustration-paper)"/>
      <stop offset="0.75" stop-color="var(--illustration-rust-soft)"/>
      <stop offset="1" stop-color="var(--paper)"/>
    </linearGradient>
    <linearGradient id="ship-tone" x1="0" y1="0" x2="0" y2="1">
      <stop offset="0" stop-color="var(--paper)"/>
      <stop offset="0.5" stop-color="var(--illustration-paper)"/>
      <stop offset="0.82" stop-color="var(--illustration-rust-soft)"/>
      <stop offset="1" stop-color="var(--paper)"/>
    </linearGradient>
  </defs>

  <rect class="cover" x="195" y="183" width="556" height="834"/>

  <rect class="illustration whale-illustration" role="img"
        aria-label="Rust-red line drawing of a whale spouting and diving among waves"
        x="196" y="288" width="140" height="144" fill="url(#whale-tone)"/>

  <rect class="illustration ship-illustration" role="img"
        aria-label="Rust-red line drawing of a three-masted sailing ship under full sail on the sea"
        x="423" y="528" width="294" height="225" fill="url(#ship-tone)"/>

  <g class="title">
    <text class="title-line dark" x="345" y="341" textLength="381" lengthAdjust="spacingAndGlyphs">LEGENDS,</text>
    <text class="title-line blue" x="372" y="417" textLength="354" lengthAdjust="spacingAndGlyphs">OYSTERS,</text>
    <text class="title-line dark" x="223" y="493" textLength="503" lengthAdjust="spacingAndGlyphs">LIGHTHOUSES,</text>
    <text class="ampersand" x="221" y="572">&amp;</text>
    <text class="title-line blue" x="223" y="645" textLength="221" lengthAdjust="spacingAndGlyphs">TIDES</text>
  </g>

  <g class="subtitle-block">
    <text class="subtitle" x="245" y="786" textLength="452" lengthAdjust="spacingAndGlyphs"><tspan class="initial">A</tspan>DVENTURES AND MISADVENTURES FROM</text>
    <text class="subtitle" x="241" y="815" textLength="465" lengthAdjust="spacingAndGlyphs">THREE CENTURIES OF LONG ISLAND HISTORY</text>
  </g>

  <line class="divider" x1="420" y1="864" x2="514" y2="864"/>

  <text class="author" x="288" y="932" textLength="371" lengthAdjust="spacing">DELPHINE HARROWGATE</text>
</svg>
</body>
</html>
```